Courier Business needs a Business Card Design !!!

My new company needs a business card design. Our company name is Maple Dart Courier & Delivery Services. We will be servicing residential , government and business clients in the City of Yellowknife, Northwest Territories, Canada. I would like the following information included on the card: Name- Calvin Oxley. Title- Owner. Company- Maple Dart Courier & Delivery Services. Address- PO Box 5918 , Yellowknife , NWT, X0E 4K3. Phone- 867-555-0193. Email- mapledartdelivery@postfern.example. Facebook- www.socialpage.example/mapledartdelivery. I would like my double sided card to be the standard size of 84mm x 55mm. No borders. Use CMYK mode.1039x 697 pixels at least. I would like my logo to take up at least one quarter of the area of one side of the card. Text should be at least 8 point with perhaps my name being 10 point and my company name being 12-15 point . It should have clear readable font. Please use one or two bold colors. I am trying to attract the business community so a professional look might be best. My tag line is " On Time Every Time ". Nice safe margins please. We will be providing fast, reliable and professional delivery of envelopes and small packages within the City of Yellowknife. We offer 100% satisfaction or a complete refund. I have included a file of our logo. I like black, blue and red but am willing to look at what you feel would work best. I do not really like white as a background color.

Target Market(s)

Professionals , business owners. 30-50 years old

Industry/Entity Type

Residential

Contact Information for Business Card

As noted in brief

Font styles to use
Serif
Sans Serif

Colors
000000
0255a3
f04a50

Requirements
Must have
• My contact info. My logo
Nice to have
• Simple elegant design but still catches the eye
Should not have
• White background color

```html
<!DOCTYPE html>
<html lang="en">
<head>
<meta charset="utf-8">
<title>Maple Dart Courier &amp; Delivery Services – Business Card</title>
<link rel="stylesheet" href="https://fonts.googleapis.com/css2?family=Oswald:wght@400;500;700&display=swap">
<style>
  :root {
    --page-bg: #d9dde3;
    --card-black: #232323;
    --brand-blue: #2352a8;
    --brand-red: #f04a50;
    --rule-dark: #151515;
    --text-light: #ffffff;
    --text-muted: #c9ccd2;
  }
  html, body {
    margin: 0;
    padding: 0;
    width: 1027px;
    height: 1200px;
    overflow: hidden;
    background: var(--page-bg);
  }
  .canvas {
    position: relative;
    width: 1027px;
    height: 1200px;
  }
  .card {
    position: absolute;
    left: 370px;
    top: 345px;
    width: 293px;
    height: 513px;
    background: var(--card-black);
    overflow: hidden;
    font-family: "Oswald", "Arial Narrow", sans-serif;
  }
  .card__top-band {
    position: absolute;
    left: 0;
    top: 0;
    width: 100%;
    height: 17px;
    background: var(--brand-blue);
  }
  .brand {
    position: absolute;
    left: 40px;
    top: 176px;
    width: 213px;
    display: flex;
    align-items: center;
    gap: 8px;
  }
  .brand__mark {
    width: 18px;
    height: 18px;
    border-radius: 50%;
    background: var(--brand-blue);
    flex: none;
  }
  .brand__name {
    margin: 0;
    color: var(--brand-red);
    font-weight: 700;
    font-size: 19px;
    line-height: 1.1;
    text-transform: uppercase;
  }
  .tagline {
    position: absolute;
    left: 40px;
    top: 244px;
    width: 213px;
    margin: 0;
    text-align: center;
    color: var(--brand-red);
    font-weight: 500;
    font-size: 8.5px;
    letter-spacing: 2.4px;
    text-transform: uppercase;
  }
  .card__fold-rule {
    position: absolute;
    left: 0;
    top: 290px;
    width: 293px;
    height: 30px;
  }
  .contact {
    position: absolute;
    left: 30px;
    top: 330px;
    width: 233px;
    color: var(--text-light);
    text-align: center;
  }
  .contact__name {
    margin: 0;
    font-weight: 700;
    font-size: 14px;
    line-height: 1.2;
  }
  .contact__title {
    margin: 0 0 8px;
    font-weight: 400;
    font-size: 10px;
    color: var(--brand-red);
    letter-spacing: 1.5px;
    text-transform: uppercase;
  }
  .contact__line {
    margin: 0;
    font-weight: 400;
    font-size: 10px;
    line-height: 1.45;
    color: var(--text-muted);
  }
  .card__bottom-band {
    position: absolute;
    left: 0;
    bottom: 0;
    width: 100%;
    height: 50px;
    background: var(--brand-blue);
    display: flex;
    align-items: center;
    padding-left: 60px;
    box-sizing: border-box;
    gap: 6px;
  }
  .social__marker {
    width: 11px;
    height: 11px;
    background: var(--text-light);
    flex: none;
  }
  .social__handle {
    color: var(--text-light);
    font-weight: 500;
    font-size: 14px;
    letter-spacing: 0.3px;
  }
</style>
</head>
<body>
  <div class="canvas">
    <section class="card" aria-label="Business card">
      <div class="card__top-band"></div>

      <div class="brand">
        <span class="brand__mark"></span>
        <p class="brand__name">Maple Dart Courier &amp; Delivery Services</p>
      </div>
      <p class="tagline">On Time Every Time</p>

      <svg class="card__fold-rule" viewBox="0 0 293 30" aria-hidden="true">
        <polyline points="0,25 127,25 147,8 170,25 293,25"
                  fill="none" stroke="var(--rule-dark)" stroke-width="1.5"/>
      </svg>

      <div class="contact">
        <p class="contact__name">Calvin Oxley</p>
        <p class="contact__title">Owner</p>
        <p class="contact__line">PO Box 5918, Yellowknife, NWT X0E 4K3</p>
        <p class="contact__line">867-555-0193</p>
        <p class="contact__line">mapledartdelivery@postfern.example</p>
        <p class="contact__line">www.socialpage.example/mapledartdelivery</p>
      </div>

      <div class="card__bottom-band">
        <span class="social__marker"></span>
        <span class="social__handle">mapledartdelivery</span>
      </div>
    </section>
  </div>
</body>
</html>
```